We are a full service general contractor that specializes in emergency services and insurance restoration/repair. Most of our work relates to water damage, fire dame, smoke, wind and hail, storm damage, etc. Pretty much anything you would call your insurance company for.

On one side of card the logo is VERY easy with the possibility of some modifications once I get a preview. I had a logo designed years ago and its on all my vehicles so I want to stick with my branding at this point and time.

Its a 2 sided card-for one side I would like the following:
* See logo (its attached)
* I would like this logo as large/big/bold as possible-essentially it should fill up the entire side of the card (barring it not looking proportionally correct of course)
* I think the background should be white behind it-or possibly red (with colors inverted so that they don't get lost in the red background)
* I'm attaching a photo of one of our work vans to go off of-you will notice that the .com wraps up the side of the logo-this .com portion needs to added on as the logo is only the crest renewal logo

The other side of the card I'm thinking should be:
* My biggest struggle is formatting-in other words-I don't know how to lay out all that info without the card looking jumbled/messy
* all our logos, vehicles, marketing media, etc. is based on or at least inspired by a clean look
* a smaller version of logo (without the .com) should be located somewhere on this side of card-I've seen some cards where its centered and others where its offset-I'm not sure which is better
* I could conceivably leave off PO BOX if its too much info and something needs deleted

The logo will display company name-other pertinent info:
Phone: 704 555 0183
Mobile: 704 555 0147
Fax: 704 555 0192
email: crestrenewal@mailhub.example
Address: 2583 Elm Rd.
Charlotte, NC
PO BOX 36502 28299

```html
<!DOCTYPE html>
<html lang="en">
<head>
<meta charset="utf-8">
<title>Crest Renewal – Business Card</title>
<link href="https://fonts.googleapis.com/css2?family=Roboto:wght@400;700&display=swap" rel="stylesheet">
<style>
  :root {
    --backdrop: #e7e4e0;
    --card: #ffffff;
    --ink: #2c3840;
    --text: #2b2b2b;
    --red: #b81e24;
    --red-dark: #8c1519;
    --rule: #4a4a4a;
  }
  * { margin: 0; padding: 0; box-sizing: border-box; }
  html, body { width: 1200px; height: 1000px; overflow: hidden; }
  body {
    background: var(--backdrop);
    font-family: "Roboto", Arial, sans-serif;
    color: var(--text);
    position: relative;
  }
  .card {
    position: absolute;
    left: 220px;
    width: 760px;
    height: 435px;
    background: var(--card);
    box-shadow: 0 2px 8px rgba(0,0,0,0.15);
    overflow: hidden;
  }
  .card--front { top: 56px; }
  .card--back { top: 508px; }

  .wordmark {
    position: absolute;
    display: flex;
    align-items: center;
    gap: 10px;
    font-weight: 700;
    color: var(--ink);
    letter-spacing: 0.5px;
    line-height: 1;
  }
  .wordmark__square { background: var(--red); flex: none; }
  .wordmark--small { right: 42px; top: 36px; font-size: 27px; }
  .wordmark--small .wordmark__square { width: 22px; height: 22px; }

  .person { position: absolute; left: 41px; top: 188px; }
  .person__name { color: var(--red); font-weight: 700; font-size: 19px; }
  .person__title { font-size: 16px; margin-top: 3px; }
  .divider {
    position: absolute; left: 41px; right: 41px; top: 249px;
    border-top: 1px solid var(--rule);
  }
  .contact-list {
    position: absolute; left: 41px; top: 268px; list-style: none;
  }
  .contact-list li {
    display: flex; align-items: center; gap: 7px;
    font-size: 16.5px; height: 27.4px;
  }
  .contact-list svg { width: 13px; height: 13px; fill: var(--red); flex: none; }
  .address {
    position: absolute; right: 63px; top: 360px;
    text-align: right; font-size: 16.5px; line-height: 22px;
  }
  .corner-tab { position: absolute; right: 0; top: 330px; }

  .wordmark--large {
    left: 0; right: 0; top: 150px;
    justify-content: center;
    font-size: 64px;
    gap: 18px;
  }
  .wordmark--large .wordmark__square { width: 44px; height: 44px; }
  .tagline {
    position: absolute; left: 0; right: 0; top: 298px;
    text-align: center; font-weight: 700; font-size: 20px;
    color: var(--ink); letter-spacing: 0.3px;
  }
  .tagline span { color: var(--ink); margin: 0 6px; }
</style>
</head>
<body>

<section class="card card--front">
  <div class="wordmark wordmark--small">
    <span class="wordmark__square"></span>
    <span class="wordmark__name">CREST RENEWAL</span>
  </div>

  <div class="person">
    <p class="person__name">Dana Whitfield</p>
    <p class="person__title">Founder</p>
  </div>
  <div class="divider"></div>

  <ul class="contact-list">
    <li><svg viewBox="0 0 16 16"><path d="M3.5 1l2.5 3-1.5 2c1 2 3 4 5 5l2-1.5 3 2.5-1.5 2.5C8 15 1 8 1 2.5z"/></svg>704 555 0183</li>
    <li><svg viewBox="0 0 16 16"><path d="M4 0h8v16H4zM5.5 2v10h5V2zM7 13h2v1.5H7z"/></svg>704 555 0147</li>
    <li><svg viewBox="0 0 16 16"><path d="M4 1h8v4H4zM1 6h14v6h-3v3H4v-3H1zM5 10v3.5h6V10z"/></svg>704 555 0192</li>
    <li><svg viewBox="0 0 16 16"><path d="M1 3h14v1L8 9 1 4zM1 6l7 5 7-5v7H1z"/></svg>crestrenewal@mailhub.example</li>
    <li><svg viewBox="0 0 16 16"><path d="M8 1a7 7 0 100 14A7 7 0 008 1zm0 1.5c.8 0 1.8 1.6 2.1 4.5H5.9C6.2 4.1 7.2 2.5 8 2.5zM2.6 7h2c.1-1.6.4-3 .9-3.9A5.5 5.5 0 002.6 7zm8.8 0h2a5.5 5.5 0 00-2.9-3.9c.5.9.8 2.3.9 3.9zM2.6 9a5.5 5.5 0 002.9 3.9c-.5-.9-.8-2.3-.9-3.9zm3.3 0c.3 2.9 1.3 4.5 2.1 4.5s1.8-1.6 2.1-4.5zm5.5 0c-.1 1.6-.4 3-.9 3.9A5.5 5.5 0 0013.4 9z"/></svg>www.crestrenewal.example</li>
  </ul>

  <p class="address">2583 Elm Rd. Charlotte, NC<br>PO BOX 36502 28299</p>

  <svg class="corner-tab" width="52" height="105" viewBox="0 0 52 105" aria-hidden="true">
    <polygon points="52,0 0,52 52,52" fill="var(--red)"/>
    <polygon points="0,52 52,52 52,105" fill="var(--red-dark)"/>
  </svg>
</section>

<section class="card card--back">
  <div class="wordmark wordmark--large">
    <span class="wordmark__square"></span>
    <span class="wordmark__name">CREST RENEWAL</span>
  </div>
  <p class="tagline">REPAIR<span>•</span>BUILD<span>•</span>RENOVATE</p>
</section>

</body>
</html>
```